Layout for site fence advertising - length approx. 250 cm x 125 cm

The advertising will later be printed on a PVC film and used for events or on sports fields.

Main services :
Your regional contact at
Real estate and business financing
independent insurance advice

```html
<!DOCTYPE html>
<html lang="en">
<head>
<meta charset="utf-8">
<title>Site Fence Banner – Regional Financing Contact</title>
<link rel="stylesheet" href="https://fonts.googleapis.com/css2?family=Montserrat:wght@700;800&family=Open+Sans:wght@400;600;700&display=swap">
<style>
  :root {
    --brand-blue: #2a55b0;
    --ink: #2b2b2b;
    --panel: #f7f8fa;
    --dark: #1c1c1e;
    --dark-soft: #3a3a3c;
    --stage: #e9eaec;
    --white: #ffffff;
  }
  * { margin: 0; padding: 0; box-sizing: border-box; }
  html, body { width: 885px; height: 1200px; overflow: hidden; background: var(--stage); }
  .canvas { position: relative; width: 885px; height: 1200px; }
  .banner { position: absolute; left: 20px; top: 389px; width: 845px; height: 422px; box-shadow: 0 10px 30px rgba(0,0,0,.25); }
  .banner svg { display: block; }
  .headline { font-family: 'Montserrat', sans-serif; font-weight: 800; }
  .body-text { font-family: 'Open Sans', sans-serif; }
</style>
</head>
<body>
<main class="canvas">
  <section class="banner">
    <svg width="845" height="422" viewBox="0 0 845 422" xmlns="http://www.w3.org/2000/svg">
      <defs>
        <linearGradient id="panel-fill" x1="0" y1="0" x2="1" y2="1">
          <stop offset="0" stop-color="#ffffff"/>
          <stop offset="1" stop-color="#eceef2"/>
        </linearGradient>
        <linearGradient id="scene-fill" x1="0" y1="0" x2="0.6" y2="1">
          <stop offset="0" stop-color="#8fa3c4"/>
          <stop offset="0.45" stop-color="#6f6a66"/>
          <stop offset="0.75" stop-color="#8a6440"/>
          <stop offset="1" stop-color="#3b2f27"/>
        </linearGradient>
        <linearGradient id="dark-fill" x1="0" y1="0" x2="1" y2="0">
          <stop offset="0" stop-color="var(--dark)"/>
          <stop offset="0.5" stop-color="var(--dark-soft)"/>
          <stop offset="1" stop-color="var(--dark)"/>
        </linearGradient>
        <linearGradient id="photo-a" x1="0" y1="0" x2="1" y2="1">
          <stop offset="0" stop-color="#dfe6ef"/><stop offset="1" stop-color="#7d8ea6"/>
        </linearGradient>
        <linearGradient id="photo-b" x1="0" y1="0" x2="1" y2="1">
          <stop offset="0" stop-color="#eee9e3"/><stop offset="1" stop-color="#b49c86"/>
        </linearGradient>
        <linearGradient id="photo-c" x1="0" y1="0" x2="1" y2="1">
          <stop offset="0" stop-color="#5c6b7c"/><stop offset="1" stop-color="#c8a57a"/>
        </linearGradient>
      </defs>

      <!-- right white panel -->
      <rect class="info-panel" x="0" y="0" width="845" height="422" fill="url(#panel-fill)"/>

      <!-- dark contact strip -->
      <path class="contact-strip" d="M330 336 H845 V422 H320 Z" fill="url(#dark-fill)"/>
      <line class="strip-rule" x1="440" y1="332" x2="845" y2="332" stroke="var(--brand-blue)" stroke-width="2.5"/>

      <!-- scene photo with curved edge -->
      <path class="scene-photo" role="img" aria-label="Photo of a modern house with a wooden terrace at dusk and a smiling advisor in a dark suit in the foreground"
            d="M0 0 H378 C430 60 445 200 420 290 C405 350 360 395 315 422 H0 Z" fill="url(#scene-fill)"/>
      <path class="accent-arc" d="M385 0 C440 60 455 200 430 290 C414 350 368 398 322 422"
            fill="none" stroke="var(--brand-blue)" stroke-width="5"/>

      <!-- round service photos -->
      <g class="service-photo">
        <circle cx="427" cy="102" r="58" fill="var(--white)"/>
        <circle cx="427" cy="102" r="54" fill="url(#photo-a)" role="img" aria-label="Photo of hands pointing at a laptop with financial charts"/>
      </g>
      <g class="service-photo">
        <circle cx="437" cy="224" r="58" fill="var(--white)"/>
        <circle cx="437" cy="224" r="54" fill="url(#photo-b)" role="img" aria-label="Photo of a happy family lying together on a rug"/>
      </g>
      <g class="service-photo">
        <circle cx="394" cy="337" r="58" fill="var(--white)"/>
        <circle cx="394" cy="337" r="54" fill="url(#photo-c)" role="img" aria-label="Photo of a hand dropping a coin into a savings jar"/>
      </g>

      <!-- brand block -->
      <g class="brand">
        <circle cx="582" cy="82" r="36" fill="none" stroke="var(--brand-blue)" stroke-width="3"/>
        <line class="brand-divider" x1="626" y1="42" x2="626" y2="119" stroke="var(--ink)" stroke-width="1.5"/>
        <text class="headline brand-name" x="634" y="77" font-size="14.5" fill="var(--brand-blue)" font-weight="700">RM Finanzberatung GmbH</text>
        <text class="body-text brand-tagline" x="634" y="94" font-size="10.5" font-weight="600" fill="var(--ink)">Finanzieren, Versichern, Vorsorgen</text>
      </g>

      <!-- headline -->
      <text class="headline" x="822" y="179" text-anchor="end" font-size="35" fill="var(--ink)">YOUR REGIONAL</text>
      <text class="headline" x="822" y="221" text-anchor="end" font-size="35" fill="var(--brand-blue)">CONTACT AT</text>

      <!-- services -->
      <text class="body-text" x="822" y="253" text-anchor="end" font-size="17" fill="var(--ink)">Real estate and business financing</text>
      <text class="body-text" x="822" y="275" text-anchor="end" font-size="17" fill="var(--ink)">independent insurance advice</text>

      <!-- call to action tab -->
      <path class="cta-tab" d="M599 312 H813 L836 347 H612 Z" fill="var(--brand-blue)"/>
      <text class="body-text" x="800" y="335" text-anchor="end" font-size="12.5" font-weight="700" letter-spacing="1.2" fill="var(--white)">CONTACT US</text>

      <!-- phone -->
      <g class="phone-icon" transform="translate(615 377)">
        <circle r="10" fill="none" stroke="var(--white)" stroke-width="1.6"/>
        <path d="M-4.5 -5 C-5.5 -2 -2 4 3.5 5 L5 3 L2.5 1 L1 2 C-1 1 -2 -1 -2 -2 L-1 -3 L-3 -6 Z" fill="var(--white)"/>
      </g>
      <text class="body-text" x="822" y="384" text-anchor="end" font-size="20" font-weight="700" fill="var(--white)">+43 600 123 4567</text>
      <text class="body-text" x="822" y="409" text-anchor="end" font-size="13" letter-spacing="1" fill="var(--white)">www.regio-finanz.at | office@regio-finanz.at</text>
    </svg>
  </section>
</main>
</body>
</html>
```